Business Card Design

I need a good card to sell my talents in the music field and get my name known as a musician/Guitarist

Industry/Entity Type

Business

Contact Information for Business Card

Leonard Vasquez Musician/Guitarist

```html
<!DOCTYPE html>
<html lang="en">
<head>
<meta charset="utf-8">
<title>Leonard Vasquez — Business Card</title>
<link href="https://fonts.googleapis.com/css2?family=Fondamento&family=Open+Sans:wght@400&display=swap" rel="stylesheet">
<style>
  :root {
    --page: #ffffff;
    --card-dark: #0c0c0c;
    --card-mid: #1e1e1e;
    --card-edge: #2a2a2a;
    --red-deep: #6e0000;
    --red: #c40b0b;
    --red-bright: #e52222;
    --ink: #ffffff;
    --ink-soft: #d8d8d8;
    --rule: rgba(255,255,255,0.28);
  }
  * { margin: 0; padding: 0; box-sizing: border-box; }
  html, body {
    width: 1200px; height: 703px; overflow: hidden;
    background: var(--page);
  }
  .sheet { position: relative; width: 1200px; height: 703px; }

  .card {
    position: absolute; top: 195px;
    width: 552px; height: 313px; overflow: hidden;
    background: radial-gradient(ellipse at 50% 55%, var(--card-mid) 0%, var(--card-dark) 70%);
    box-shadow: 0 0 0 1px var(--card-edge);
  }
  .card--front { left: 30px; }
  .card--back { left: 618px; }

  .gloss {
    position: absolute; inset: 0; width: 100%; height: 100%;
  }

  .side-band {
    position: absolute; top: 78px; width: 35px; height: 156px;
    background: linear-gradient(90deg, var(--red-deep), var(--red) 45%, var(--red-bright) 60%, var(--red-deep));
  }
  .side-band--left { left: 0; }
  .side-band--right { right: 0; }

  .music-mark {
    position: absolute; left: 214px; top: 57px; width: 136px; height: 81px;
    background: linear-gradient(180deg, #f2f2f2, #cfcfcf);
    border-radius: 4px; opacity: 0.92;
  }

  .rule {
    position: absolute; left: 48px; width: 454px; height: 1px;
    background: linear-gradient(90deg, transparent, var(--rule) 10%, var(--rule) 90%, transparent);
  }
  .rule--top { top: 161px; }
  .rule--bottom { top: 227px; }

  .name {
    position: absolute; left: 0; width: 100%; top: 174px;
    text-align: center; color: var(--ink);
    font-family: "Fondamento", serif; font-size: 29px; line-height: 1;
  }
  .role {
    position: absolute; left: 0; width: 100%; top: 209px;
    text-align: center; color: var(--ink-soft);
    font-family: "Open Sans", sans-serif; font-size: 10.5px; line-height: 1;
  }
  .contact {
    position: absolute; left: 0; width: 100%; top: 250px;
    text-align: center; color: var(--ink);
    font-family: "Fondamento", serif; font-size: 19px; line-height: 1;
    white-space: nowrap;
  }
  .contact .sep { padding: 0 5px; font-family: "Open Sans", sans-serif; }

  .back-band {
    position: absolute; left: 0; top: 78px; width: 100%; height: 158px;
    background: linear-gradient(180deg, var(--red-deep), var(--red) 20%, var(--red-bright) 40%, var(--red) 70%, var(--red-deep));
  }
  .back-strip {
    position: absolute; left: 0; top: 131px; width: 100%; height: 50px;
    background: linear-gradient(90deg, #3a0000, #151515 25%, #202020 50%, #151515 75%, #3a0000);
  }
</style>
</head>
<body>
<main class="sheet">

  <section class="card card--front" aria-label="Business card front">
    <svg class="gloss" viewBox="0 0 552 313" aria-hidden="true">
      <polygon points="330,0 552,0 552,95" fill="rgba(255,255,255,0.07)"/>
      <polygon points="0,0 552,0 552,16 0,48" fill="rgba(255,255,255,0.04)"/>
    </svg>
    <div class="side-band side-band--left" role="img" aria-label="Red diamond lattice pattern"></div>
    <div class="side-band side-band--right" role="img" aria-label="Red diamond lattice pattern"></div>
    <div class="music-mark" role="img" aria-label="White music staff with treble clef and notes"></div>
    <div class="rule rule--top"></div>
    <h1 class="name">Leonard Vasquez</h1>
    <p class="role">Musician | Guitarist</p>
    <div class="rule rule--bottom"></div>
    <p class="contact">leonardvasquez.com<span class="sep">|</span>@leonardv<span class="sep">|</span>0912-478-350</p>
  </section>

  <section class="card card--back" aria-label="Business card back">
    <div class="back-band" role="img" aria-label="Red diamond lattice pattern band"></div>
    <div class="back-strip" role="img" aria-label="Dark lattice pattern strip"></div>
  </section>

</main>
</body>
</html>
```